Branding website for a Data Science company with 1 product

Branding website for a Data Science company, featuring our main product: Quorlink. The purpose of the website is to get potential clients to get a peek at what we do, but the main purpose is to get them to get in touch with us. The website will not answer all questions. Therefore the contact details and contact form is a must-have .

Target Market(s)

Potential new B2B clients with medium to large websites, application users (behind a login)

Industry/Entity Type

It Company

Coding

Coded - Design and coding required

Number of Pages Required

2 page

Font styles to use
Sans Serif

Colors

Designer to choose colors to be used in the design.

Requirements
Must have
• A contact form and branding a product

```html
<!DOCTYPE html>
<html lang="en">
<head>
<meta charset="utf-8">
<title>Quorlink · Tallyfold Partners</title>
<link rel="stylesheet" href="https://fonts.googleapis.com/css2?family=Archivo+Black&family=Libre+Franklin:wght@400;600;700&family=Montserrat:wght@500&display=swap">
<style>
  :root{
    --orange:#f15a22;
    --black:#000;
    --grey-head:#8c8c8c;
    --grey-text:#4a4a4a;
    --grey-logo:#a9a9a9;
    --white:#fff;
  }
  *{box-sizing:border-box;margin:0;padding:0}
  html,body{width:1200px;height:1115px;overflow:hidden;background:var(--white)}
  body{position:relative;font-family:"Libre Franklin",Arial,sans-serif;color:var(--grey-text)}
  .abs{position:absolute}

  /* header */
  .topbar{left:0;top:0;width:1200px;height:4px;background:var(--orange)}
  .brand{left:206px;top:24px;display:flex;align-items:center;gap:10px}
  .brand-dot{width:22px;height:22px;border-radius:50%;background:var(--orange)}
  .brand-name{font-size:24px;font-weight:400;color:var(--orange);letter-spacing:1px}
  .contact-line{right:147px;top:18px;font-size:12px;font-weight:600;color:var(--orange);display:flex;gap:18px}
  .nav{right:147px;top:44px;display:flex;gap:14px;font-size:10.5px;letter-spacing:1.2px;color:#555}
  .nav .active{color:#111;font-weight:700;position:relative}
  .nav .active::after{content:"";position:absolute;left:0;right:0;top:21px;height:2px;background:#777}

  /* hero */
  .hero{left:0;top:75px;width:1200px;height:374px;background:var(--black);overflow:hidden}
  .hero-mark{left:316px;top:49px;width:132px;height:120px;background:radial-gradient(ellipse at center,rgba(241,90,34,.55) 0%,rgba(241,90,34,.18) 55%,rgba(241,90,34,0) 75%)}
  .hero-tagline{left:280px;top:178px;width:204px;text-align:center;color:#ddd;font-size:10px;line-height:13px}
  .hero-vertical{left:488px;top:78px;writing-mode:vertical-rl;transform:rotate(180deg);color:var(--orange);font-size:9px;font-weight:700;letter-spacing:1px}
  .frame-thin{left:558px;top:31px;width:437px;height:330px;border:1px solid var(--orange)}
  .frame-main{left:574px;top:47px;width:436px;height:276px;border:4px solid var(--orange);background:#000}
  .hero-photo{width:100%;height:100%;background:linear-gradient(110deg,#0f4a63 0%,#3fa6c4 22%,#14313f 38%,#c21a24 50%,#5a0f14 62%,#1a4a5c 75%,#52b8d6 100%)}
  .hero-title{left:208px;top:296px;font-family:"Archivo Black",Arial,sans-serif;font-size:84px;line-height:1;color:var(--white);letter-spacing:-2px;white-space:nowrap}

  /* who we are */
  .card-back{left:248px;top:500px;width:298px;height:192px;border:1px solid #e2e2e2}
  .video-card{left:266px;top:520px;width:299px;height:191px;background:var(--white);box-shadow:0 2px 8px rgba(0,0,0,.18)}
  .video-person{right:10px;top:10px;width:170px;height:171px;background:linear-gradient(180deg,#f4f4f4 0%,#c9a48f 35%,#8d8d8d 70%,#7a7a7a 100%)}
  .video-play{left:121px;top:74px}
  .video-name{left:19px;top:147px;font-size:11px;color:#222}
  .video-role{left:19px;top:161px;font-size:8px;line-height:10px;color:#555}
  .section-title{font-family:"Montserrat",Arial,sans-serif;font-weight:500;color:var(--grey-head)}
  .who-title{left:612px;top:508px;font-size:44px}
  .rule{height:3px;background:var(--orange)}
  .who-rule{left:610px;top:569px;width:128px}
  .who-text{left:611px;top:590px;width:390px;font-size:11px;line-height:14.5px}
  .btn{left:612px;top:670px;width:131px;height:34px;background:var(--orange);color:var(--white);font-size:12px;font-weight:700;display:flex;align-items:center;justify-content:center;letter-spacing:.3px}

  /* clients */
  .clients{left:230px;top:720px;width:810px;height:122px;background:linear-gradient(180deg,#fff 0%,#f6f6f6 50%,#fff 100%);border-bottom:1px dotted #d8d8d8}
  .client{top:61px;transform:translate(-50%,-50%);font-size:13px;font-weight:600;color:var(--grey-logo)}

  /* what we do */
  .what-title{left:0;width:1236px;top:886px;font-size:44px;text-align:center}
  .what-rule{left:544px;top:946px;width:127px}
  .spine{left:604px;top:970px;width:1px;height:145px;background:#999}
  .connector{height:1px;background:#999}
  .node{width:7px;height:7px;border-radius:50%;background:#888}
  .service-name{font-size:20px;font-weight:700;color:var(--orange)}
  .service-text{font-size:11px;line-height:14.5px;text-align:center}
</style>
</head>
<body>
  <div class="abs topbar"></div>

  <header>
    <div class="abs brand"><span class="brand-dot"></span><span class="brand-name">Tallyfold Partners</span></div>
    <div class="abs contact-line"><span>T: +31(0)6 55502187</span><span>E: hello@tallyfold.example</span><span>KvK: 00.11.22.33</span></div>
    <nav class="abs nav"><span class="active">HOME</span><span>ABOUT US</span><span>PRODUCTS</span><span>CONTACT US</span></nav>
  </header>

  <section class="abs hero">
    <div class="abs hero-mark" role="img" aria-label="Orange network illustration of linked nodes representing the product"></div>
    <p class="abs hero-tagline">software-as-a-service to capture, learn and target our client's website visitors and turn them into loyal customers.</p>
    <div class="abs hero-vertical">A DATA SCIENCE COMPANY</div>
    <div class="abs frame-thin"></div>
    <div class="abs frame-main"><div class="hero-photo" role="img" aria-label="Digital padlocks over streams of encrypted code, one red lock between blue ones"></div></div>
    <h1 class="abs hero-title">QUORLINK</h1>
  </section>

  <section>
    <div class="abs card-back"></div>
    <div class="abs video-card">
      <div class="abs video-person" role="img" aria-label="Video still of the company spokesperson in a grey T-shirt"></div>
      <svg class="abs video-play" width="42" height="42" viewBox="0 0 42 42"><circle cx="21" cy="21" r="19" fill="#fff" stroke="#111" stroke-width="3"/><path d="M16 12 L30 21 L16 30 Z" fill="#111"/></svg>
      <div class="abs video-name">Marten Oakes</div>
      <div class="abs video-role">Senior Vice President<br>Design</div>
    </div>
    <h2 class="abs section-title who-title">Who we are?</h2>
    <div class="abs rule who-rule"></div>
    <p class="abs who-text">We believe that every company needs data science and algorithms to stay on top of today's overwhelming speed of innovation. We advise and help to turn your company into a data driven company by making data science comprehensible and usable for everybody in your organization.</p>
    <div class="abs btn">READ MORE</div>
  </section>

  <section class="abs clients">
    <span class="abs client" style="left:154px">Voltra</span>
    <span class="abs client" style="left:257px">Kesto</span>
    <span class="abs client" style="left:363px">Wayline</span>
    <span class="abs client" style="left:468px">Orvane</span>
    <span class="abs client" style="left:572px">Lumetra</span>
    <span class="abs client" style="left:677px">Medira</span>
  </section>

  <section>
    <h2 class="abs section-title what-title">What do we do?</h2>
    <div class="abs rule what-rule"></div>
    <div class="abs spine"></div>

    <svg class="abs" style="left:438px;top:958px" width="80" height="76" viewBox="0 0 80 76">
      <path d="M36 4 C16 4 4 15 4 28 C4 36 9 42 16 46 L12 60 L26 50 C30 51 33 51 36 51" fill="none" stroke="#aaa" stroke-width="5"/>
      <path d="M50 26 C66 26 78 34 78 45 C78 53 73 58 66 61 L68 73 L56 63 C54 64 52 64 50 64 C34 64 22 56 22 45 C22 34 34 26 50 26 Z" fill="#aaa"/>
    </svg>
    <div class="abs node" style="left:516px;top:991px"></div>
    <div class="abs connector" style="left:520px;top:994px;width:84px"></div>
    <div class="abs service-name" style="left:440px;top:1036px">Advisory</div>
    <p class="abs service-text" style="left:216px;top:1073px;width:308px">Data science comes in many flavors. Which one fits your company best? Taking all costs, benefits and organizational impact into account? We can help you with formulating a</p>

    <div class="abs connector" style="left:604px;top:1037px;width:86px"></div>
    <svg class="abs" style="left:686px;top:990px" width="86" height="90" viewBox="0 0 86 90" fill="none" stroke="#aaa" stroke-width="3">
      <line x1="42" y1="45" x2="74" y2="10"/><line x1="42" y1="45" x2="18" y2="12"/><line x1="42" y1="45" x2="50" y2="76"/>
      <line x1="42" y1="45" x2="78" y2="62"/><line x1="42" y1="45" x2="14" y2="55"/>
      <circle cx="42" cy="45" r="8"/><circle cx="74" cy="9" r="6"/><circle cx="50" cy="78" r="6"/>
      <circle cx="18" cy="9" r="4" fill="#aaa"/><circle cx="79" cy="62" r="4" fill="#aaa"/><circle cx="14" cy="55" r="4" fill="#aaa"/>
    </svg>
    <div class="abs service-name" style="left:694px;top:1084px">Insights</div>
  </section>
</body>
</html>
```